Namecard Designs+Logo for a High End Automobile Company

We need a new business card for our company called Velta Motorhof.

www.veltamotorhof.example.sg
Our new website will be up in 2.5 months time.

We sell used and brand new continental cars like Korvane, QTL, Dravell, Solbrini and etc. Currently we are operating from 2 offices in Singapore and United Kingdom.

We want a design which is serious. We are open to colours but try to keep it at a maximum of 3 colours.

We prefer something simple and minimal. We are open to 2 sides printing or even 2 sided namecards. Both UK and Singapore company offices address must be in; either side by side, front and back, or even 2 sided cards.

The logo can be a text logo, emblem, abstract, pictorial or combination.

We are printing with Pribo.com so please kindly follow the printing guideline.

http://uk.pribo.example/help/faq/templates-and-guidelines.html

Rich and Car Enthusiasts

Printing

Must have
• Our 2 offices; UK and Singapore.

Our slogan which is " The Automobile Specialist"
Should not have
• Not more than 3 colours

```html
<!DOCTYPE html>
<html lang="en">
<head>
<meta charset="utf-8">
<title>Velta Motorhof — Business Card</title>
<link href="https://fonts.googleapis.com/css2?family=Arimo:wght@400;700&display=swap" rel="stylesheet">
<style>
  :root {
    --backdrop: #262829;
    --card-white: #ffffff;
    --brand-navy: #0d3b86;
    --brand-blue: #1679c2;
    --deep-navy: #0a2a66;
    --ink: #1b1f2a;
    --silver-light: #f4f5f7;
    --silver-mid: #a7adb6;
    --silver-dark: #6d737c;
  }
  * { margin: 0; padding: 0; box-sizing: border-box; }
  html, body {
    width: 1200px;
    height: 1200px;
    overflow: hidden;
    background: var(--backdrop);
    font-family: "Arimo", Arial, sans-serif;
  }
  .canvas { position: relative; width: 1200px; height: 1200px; }
  .card {
    position: absolute;
    left: 282px;
    width: 636px;
    height: 386px;
    overflow: hidden;
  }
  .card svg.card-art { position: absolute; inset: 0; width: 100%; height: 100%; }

  /* Front */
  .card--front { top: 203px; background: var(--card-white); }
  .brand {
    position: absolute;
    left: 0; right: 0;
    top: 64px;
    text-align: center;
  }
  .brand__name {
    font-weight: 700;
    font-size: 37px;
    letter-spacing: -0.5px;
    color: var(--brand-navy);
    line-height: 1;
  }
  .brand__slogan {
    margin: 6px auto 0;
    display: inline-block;
    font-size: 16px;
    color: var(--ink);
    border-top: 2px solid var(--brand-navy);
    padding: 1px 10px 0;
    line-height: 1.1;
  }
  .office {
    position: absolute;
    top: 150px;
    width: 260px;
    font-weight: 700;
    font-size: 14px;
    line-height: 22px;
    color: var(--ink);
  }
  .office--uk { left: 36px; }
  .office--sg { left: 340px; }
  .office__address { font-style: normal; }
  .office__lines { margin-top: 10px; }

  /* Back */
  .card--back {
    top: 611px;
    background: linear-gradient(100deg, var(--brand-blue) 0%, #114f9e 40%, var(--deep-navy) 100%);
  }
  .back-brand { position: absolute; left: 24px; top: 230px; color: var(--card-white); }
  .back-brand__name { font-weight: 700; font-size: 44px; letter-spacing: -0.5px; line-height: 1; }
  .back-brand__slogan { font-size: 20px; margin-top: 6px; padding-left: 12px; }
</style>
</head>
<body>
<main class="canvas">

  <section class="card card--front" aria-label="Business card front">
    <svg class="card-art" viewBox="0 0 636 386" aria-hidden="true">
      <defs>
        <linearGradient id="silverFront" x1="0" y1="0" x2="1" y2="0">
          <stop offset="0" stop-color="var(--silver-mid)"/>
          <stop offset="0.45" stop-color="var(--silver-light)"/>
          <stop offset="0.8" stop-color="var(--silver-dark)"/>
          <stop offset="1" stop-color="var(--silver-light)"/>
        </linearGradient>
        <linearGradient id="blueFront" x1="0" y1="0" x2="1" y2="0">
          <stop offset="0" stop-color="var(--brand-blue)"/>
          <stop offset="1" stop-color="var(--deep-navy)"/>
        </linearGradient>
      </defs>
      <path d="M0 330 C 210 342, 450 310, 636 226 L636 386 L0 386 Z" fill="url(#silverFront)"/>
      <path d="M0 346 C 230 356, 470 328, 636 258 L636 386 L0 386 Z" fill="url(#blueFront)"/>
    </svg>

    <div class="brand">
      <div class="brand__name">Velta Motorhof</div>
      <div class="brand__slogan">The Automobile Specialist</div>
    </div>

    <div class="office office--uk">
      <address class="office__address">218 Marlow Crescent, Suite 310<br>Halden Park, HP4 7QX, United Kingdom</address>
      <div class="office__lines">T:+44 (0) 120 555 0147<br>F:+44 (0) 120 555 0148</div>
    </div>
    <div class="office office--sg">
      <address class="office__address">40 Kestrel Quay, #08-12<br>Singapore 049871</address>
      <div class="office__lines">T:+65 6555 0182<br>F:+65 6555 0183</div>
    </div>
  </section>

  <section class="card card--back" aria-label="Business card back">
    <svg class="card-art" viewBox="0 0 636 386" aria-hidden="true">
      <defs>
        <linearGradient id="silverBack" x1="0" y1="0" x2="1" y2="0">
          <stop offset="0" stop-color="var(--silver-dark)"/>
          <stop offset="0.35" stop-color="var(--silver-light)"/>
          <stop offset="0.7" stop-color="var(--silver-mid)"/>
          <stop offset="1" stop-color="var(--silver-light)"/>
        </linearGradient>
      </defs>
      <path d="M0 322 C 200 334, 440 282, 636 196 L636 214 C 450 298, 220 352, 0 342 Z" fill="url(#silverBack)"/>
      <path d="M0 368 C 220 376, 470 330, 636 262 L636 272 C 470 344, 220 386, 0 380 Z" fill="url(#silverBack)" opacity="0.85"/>
    </svg>

    <div class="back-brand">
      <div class="back-brand__name">Velta Motorhof</div>
      <div class="back-brand__slogan">The Automobile Specialist</div>
    </div>
  </section>

</main>
</body>
</html>
```